Store Fixtures Company Business Card Design

We are looking for a business card design for a store fixture company. "Bright Shelf Retail Outfitters" we help small businesses with their start up by providing fixtures required to display their products.
It should have a simple yet innovative design in the front, and a couple of sketch design for some sample products we carry in the back, to give a refined look to our company.
We would like our logo, do have one of our products "display cases" integrated in the design. And the rest of it just a clean look, which gives our address, store hours, and contact number, etc.
The color scheme as seen in the samples can be changed as long as the goal is achieved. The design attached just doesn't give off the direction we are looking to go.
Any off the attached products can be used as sketches in the back design. We do not want any name in the front.

```html
<!DOCTYPE html>
<html lang="en">
<head>
<meta charset="utf-8">
<title>Bright Shelf Retail Outfitters – Business Card</title>
<link rel="stylesheet" href="https://fonts.googleapis.com/css2?family=Open+Sans:wght@400;600;800&display=swap">
<style>
  :root {
    --bg: #e9e9ea;
    --card: #ffffff;
    --ink: #1a1a1a;
    --grey: #8c8c8c;
    --rule: #9a9a9a;
    --metal-light: #d9dadc;
    --metal-dark: #6d6f73;
  }
  * { margin: 0; padding: 0; box-sizing: border-box; }
  html, body { width: 1200px; height: 800px; overflow: hidden; }
  body {
    background: var(--bg);
    font-family: "Open Sans", Arial, sans-serif;
    color: var(--ink);
    display: flex;
    align-items: center;
    justify-content: center;
    gap: 40px;
  }
  .card {
    width: 540px;
    height: 310px;
    background: var(--card);
    box-shadow: 0 10px 30px rgba(0,0,0,.18);
    position: relative;
  }
  /* Front */
  .card--front {
    display: flex;
    align-items: center;
    justify-content: center;
  }
  .brand { display: flex; align-items: center; gap: 14px; }
  .brand__dot {
    width: 54px; height: 54px;
    border-radius: 50%;
    border: 4px solid var(--grey);
    flex: none;
  }
  .brand__text { display: flex; flex-direction: column; }
  .brand__name {
    font-weight: 800;
    font-size: 22px;
    line-height: 1.1;
    color: var(--ink);
    max-width: 240px;
  }
  .brand__tagline {
    font-size: 7.5px;
    font-weight: 600;
    letter-spacing: .18em;
    text-transform: uppercase;
    color: var(--ink);
    margin-top: 5px;
  }
  /* Back */
  .card--back { display: flex; padding: 26px 30px 24px 24px; }
  .product {
    width: 220px;
    height: 100%;
    display: flex;
    align-items: flex-end;
  }
  .product__art {
    width: 200px;
    height: 210px;
    background: linear-gradient(160deg, var(--metal-light), #f4f4f5 55%, var(--metal-dark));
    border-radius: 4px;
  }
  .info { flex: 1; padding-left: 26px; display: flex; flex-direction: column; }
  .info .brand__name { font-size: 17px; max-width: 230px; }
  .info .brand__tagline { font-size: 6px; }
  .details { margin-top: 14px; font-size: 12px; line-height: 1.5; }
  .details dt { display: inline; color: var(--grey); }
  .details dd { display: inline; }
  .details .row { display: block; }
  .rule { border: 0; border-top: 1px solid var(--rule); margin: 9px 0; }
  .web { font-size: 12px; }
  .hours { font-size: 12px; line-height: 1.5; }
  .hours .label { color: var(--grey); }
</style>
</head>
<body>
  <section class="card card--front" aria-label="Card front">
    <div class="brand">
      <span class="brand__dot"></span>
      <div class="brand__text">
        <span class="brand__name">Bright Shelf Retail Outfitters</span>
        <span class="brand__tagline">Grow your business the right way</span>
      </div>
    </div>
  </section>

  <section class="card card--back" aria-label="Card back">
    <div class="product">
      <svg class="product__art" role="img" aria-label="Photo of a rolling chrome garment rack with a branded sign panel" viewBox="0 0 200 210">
        <rect width="200" height="210" fill="none"/>
      </svg>
    </div>
    <div class="info">
      <span class="brand__name">Bright Shelf Retail Outfitters</span>
      <span class="brand__tagline">Grow your business the right way</span>
      <div class="details">
        <span class="row">4518 Maple Crest Dr, Austin, TX 78745</span>
        <span class="row"><dt>Phone: </dt><dd>512.555.0142</dd></span>
        <span class="row"><dt>Fax: </dt><dd>512.555.0187</dd></span>
      </div>
      <hr class="rule">
      <div class="web">www.brightshelfretail.com</div>
      <hr class="rule">
      <div class="hours">
        <div><span class="label">Mon-Fri:</span> 9:30 a.m. - 6:00 p.m.</div>
        <div><span class="label">Satur:</span> 10:00 a.m. - 3 p.m.</div>
      </div>
    </div>
  </section>
</body>
</html>
```